Business Card Design Project

Double-side business card.
Side One:
Logo (Including the word TOLVEKA that is part of the Logo
"Programas de Renovación Urbana y Cuidado del Entorno Natural Andino"
Side Two:
Marcela Ostrander
Co-Founder & CEO
Washington, DC (USA)
email: marcelao@tolveka.example (please use an icon for "emal")
cell: +1 (202) 555 0147 (please use an icon for "cell")
skype: marceostrander (please use an icon for "skype")
twitter: marceostrander (please use an icon for "twitter")
www.tolveka.example
Target Market(s)
Foundations, Governments, and Private sector companies that implement projects for sustainability.
Industry/Entity Type
Business
Font styles to use
Colors
Designer to choose colors to be used in the design.
Requirements
Nice to have
- barcode

```html
<!DOCTYPE html>
<html lang="es">
<head>
<meta charset="utf-8">
<title>TOLVEKA — Business Card</title>
<link href="https://fonts.googleapis.com/css2?family=Lato:wght@300;400;700;900&display=swap" rel="stylesheet">
<style>
  :root {
    --stage: #3a3a3c;
    --paper: #f7f3f1;
    --wash-teal: rgba(120, 200, 205, 0.35);
    --wash-pink: rgba(240, 190, 205, 0.35);
    --wash-peach: rgba(250, 215, 180, 0.35);
    --wash-lilac: rgba(195, 180, 225, 0.3);
    --band-red: #e24a34;
    --accent-yellow: #f7c73b;
    --ink: #1a1a1a;
    --logo-grey: #7d7f84;
    --white: #ffffff;
    --sky-purple: #9b7ab8;
    --sky-blue: #3fb6e0;
    --sky-green: #4fba7e;
    --sky-orange: #e8843a;
    --sky-lime: #b5cf3a;
  }
  * { box-sizing: border-box; margin: 0; padding: 0; }
  html, body { width: 1200px; height: 926px; overflow: hidden; }
  body {
    background: var(--stage);
    font-family: "Lato", sans-serif;
    position: relative;
  }
  .card {
    position: absolute;
    left: 220px;
    width: 760px;
    height: 434px;
    overflow: hidden;
    background:
      radial-gradient(ellipse 260px 160px at 30% 55%, var(--wash-teal), transparent 70%),
      radial-gradient(ellipse 300px 180px at 75% 30%, var(--wash-pink), transparent 70%),
      radial-gradient(ellipse 240px 150px at 20% 20%, var(--wash-peach), transparent 70%),
      radial-gradient(ellipse 220px 140px at 85% 70%, var(--wash-lilac), transparent 70%),
      var(--paper);
    box-shadow: 0 6px 18px rgba(0,0,0,0.45);
  }
  .card--front { top: 20px; }
  .card--back { top: 472px; }

  /* Front */
  .front-band { position: absolute; inset: 0; }
  .front-logo {
    position: absolute;
    top: 120px;
    left: 0;
    width: 760px;
    text-align: center;
    font-weight: 300;
    font-size: 74px;
    letter-spacing: 6px;
    color: var(--logo-grey);
  }
  .front-tagline {
    position: absolute;
    right: 54px;
    top: 338px;
    width: 520px;
    text-align: right;
    color: var(--white);
    font-size: 21px;
    line-height: 1.35;
    letter-spacing: 1px;
    font-weight: 400;
  }

  /* Back */
  .back-logo {
    position: absolute;
    top: 46px;
    left: 46px;
    font-weight: 300;
    font-size: 30px;
    letter-spacing: 3px;
    color: var(--logo-grey);
  }
  .person-name {
    position: absolute;
    top: 98px;
    left: 46px;
    font-weight: 700;
    font-size: 36px;
    letter-spacing: 0.5px;
    color: var(--ink);
    text-transform: uppercase;
  }
  .person-title {
    position: absolute;
    top: 144px;
    left: 46px;
    font-size: 17px;
    color: var(--ink);
  }
  .contact-list {
    position: absolute;
    top: 182px;
    left: 46px;
    list-style: none;
  }
  .contact-item {
    display: flex;
    align-items: center;
    gap: 10px;
    font-size: 21px;
    line-height: 28px;
    color: var(--ink);
  }
  .contact-icon {
    width: 18px;
    height: 18px;
    flex: none;
  }
  .skyline {
    position: absolute;
    right: 16px;
    bottom: 86px;
    width: 230px;
    height: 150px;
    background: linear-gradient(90deg, var(--sky-purple), var(--sky-blue) 30%, var(--sky-green) 50%, var(--sky-orange) 75%, var(--sky-lime));
    opacity: 0.85;
  }
  .back-band {
    position: absolute;
    left: 0;
    bottom: 0;
    width: 760px;
    height: 86px;
    background: var(--band-red);
  }
  .back-band::before {
    content: "";
    position: absolute;
    left: 0;
    right: 0;
    top: -8px;
    height: 4px;
    background: var(--band-red);
  }
  .city-label {
    position: absolute;
    left: 46px;
    top: 18px;
    color: var(--white);
    font-size: 19px;
    font-weight: 700;
    letter-spacing: 4px;
  }
</style>
</head>
<body>

  <section class="card card--front" aria-label="Card front">
    <svg class="front-band" width="760" height="434" viewBox="0 0 760 434" aria-hidden="true">
      <path d="M0 286 Q 380 250 760 330" fill="none" stroke="var(--accent-yellow)" stroke-width="8"/>
      <path d="M0 306 Q 380 272 760 352 L760 434 L0 434 Z" fill="var(--band-red)"/>
    </svg>
    <div class="front-logo">TOLVEKA</div>
    <p class="front-tagline">Programas de Renovación Urbana<br>y Cuidado del Entorno Natural Andino</p>
  </section>

  <section class="card card--back" aria-label="Card back">
    <div class="back-logo">TOLVEKA</div>
    <h1 class="person-name">Marcela Ostrander</h1>
    <p class="person-title">Co-Founder &amp; CEO</p>
    <ul class="contact-list">
      <li class="contact-item">
        <svg class="contact-icon" viewBox="0 0 18 18" aria-label="email"><circle cx="9" cy="9" r="9" fill="var(--ink)"/><rect x="4.5" y="6" width="9" height="6.5" fill="none" stroke="var(--white)" stroke-width="1.2"/><path d="M4.5 6 L9 9.5 L13.5 6" fill="none" stroke="var(--white)" stroke-width="1.2"/></svg>
        marcelao@tolveka.example
      </li>
      <li class="contact-item">
        <svg class="contact-icon" viewBox="0 0 18 18" aria-label="cell"><circle cx="9" cy="9" r="9" fill="var(--ink)"/><rect x="6" y="3.8" width="6" height="10.4" rx="1" fill="none" stroke="var(--white)" stroke-width="1.2"/><circle cx="9" cy="12" r="0.8" fill="var(--white)"/></svg>
        +1 (202) 555 0147
      </li>
      <li class="contact-item">
        <svg class="contact-icon" viewBox="0 0 18 18" aria-label="skype"><circle cx="9" cy="9" r="9" fill="var(--ink)"/></svg>
        marceostrander
      </li>
      <li class="contact-item">
        <svg class="contact-icon" viewBox="0 0 18 18" aria-label="twitter"><circle cx="9" cy="9" r="9" fill="var(--ink)"/></svg>
        marceostrander
      </li>
    </ul>
    <div class="skyline" role="img" aria-label="Colourful city skyline illustration with a cyclist"></div>
    <div class="back-band">
      <span class="city-label">WASHINGTON, DC (USA)</span>
    </div>
  </section>

</body>
</html>
```